Design and Renovation Company Luxury Business Card

I want to create a luxury business card for a Design and Renovation Firm . We will use our current logo. The company name is 742BUILD. We do not want anything standard. We need a very unique concept.
Please see uploaded inspiration. I really like the textured paper option. I would like the card to be thick with debossing, and/or embossing options. The logo has orange in it but I would like to see the card with and without the orange. I think the orange may make the company feel less high-end. The goal is to elevate the logo not match its vibe per se of the logo. We want something very unique, not standard at all!
I would like a space for :
Logo,
Name,
Position,
Email,
Office number,
Website Address,
Business Address,
Thank you!
Have fun!
Target Market(s)
Home owners Age 35 +
Industry/Entity Type
Design and Renovation
Contact Information for Business Card
Logo, Name, Position, Email, Office number, Website Address, Business Address,.
Colors
Designer to choose colors to be used in the design.
Requirements
Must have
- A luxury designer feel. Must be black or dark grey but open to other luxury ideas.
Nice to have
- Gold, silver, black embossing or debossing. Textured paper design.
Should not have
- A cheap look and feel.

```html
<!DOCTYPE html>
<html lang="en">
<head>
<meta charset="utf-8">
<title>742BUILD Business Card</title>
<link href="https://fonts.googleapis.com/css2?family=Montserrat:wght@500;700&family=Lato:wght@400&display=swap" rel="stylesheet">
<style>
  :root {
    --backdrop: #e0e0e0;
    --card: #262626;
    --card-deep: #1f1f1f;
    --accent: #f7941d;
    --ink: #ffffff;
    --lettering-zone: #3a3a3a;
  }
  * { margin: 0; padding: 0; box-sizing: border-box; }
  html, body {
    width: 1200px; height: 1000px; overflow: hidden;
    background: var(--backdrop);
  }
  .canvas { position: relative; width: 1200px; height: 1000px; }
  .card {
    position: absolute; left: 203px; width: 794px; height: 453px;
    border-radius: 18px; overflow: hidden;
  }
  .card--front { top: 40px; background: radial-gradient(ellipse at 50% 45%, #2e2e2e 0%, var(--card-deep) 100%); }
  .card--back { top: 506px; background: var(--card); }

  .brand__name {
    font-family: "Montserrat", sans-serif; font-weight: 500;
    color: var(--ink); letter-spacing: 2px; line-height: 1; white-space: nowrap;
  }
  .brand--front {
    position: absolute; left: 0; right: 0; top: 200px; text-align: center;
  }
  .brand--front .brand__name { font-size: 38px; }
  .brand__tagline {
    margin-top: 10px;
    font-family: "Montserrat", sans-serif; font-weight: 500;
    font-size: 10px; letter-spacing: 1.4px; color: var(--ink);
  }
  .brand--back { position: absolute; right: 29px; top: 108px; }
  .brand--back .brand__name { font-size: 15px; letter-spacing: 1.5px; }

  .person { position: absolute; right: 447px; top: 187px; text-align: right; }
  .person__name {
    font-family: "Montserrat", sans-serif; font-weight: 700;
    font-size: 36px; color: var(--accent); line-height: 1.1; letter-spacing: 0.5px;
    white-space: nowrap;
  }
  .person__role {
    font-family: "Montserrat", sans-serif; font-weight: 500;
    font-size: 18px; color: var(--ink); margin-top: 4px;
  }

  .contacts { position: absolute; left: 417px; top: 163px; list-style: none; }
  .contacts__item {
    display: flex; align-items: center; height: 35px;
    font-family: "Lato", sans-serif; font-size: 21px; color: var(--ink);
    white-space: nowrap;
  }
  .contacts__icon { width: 24px; height: 24px; margin-right: 13px; flex: none; }

  .address {
    position: absolute; left: 29px; top: 406px; display: flex; align-items: center;
    font-family: "Lato", sans-serif; font-size: 18px; color: var(--ink);
    white-space: nowrap;
  }
  .address__pin { width: 14px; height: 19px; margin-right: 6px; }

  .sign-off {
    position: absolute; left: 459px; top: 346px; width: 283px; height: 88px;
    border-radius: 10px; background: var(--lettering-zone); opacity: 0.6;
  }
</style>
</head>
<body>
<main class="canvas">
  <section class="card card--front" aria-label="Card front">
    <div class="brand brand--front">
      <p class="brand__name">742BUILD</p>
      <p class="brand__tagline">Design and Renovation Firm</p>
    </div>
  </section>

  <section class="card card--back" aria-label="Card back">
    <div class="brand brand--back">
      <span class="brand__name">742BUILD</span>
    </div>

    <div class="person">
      <h1 class="person__name">CLARA VOSS</h1>
      <p class="person__role">Managing Director</p>
    </div>

    <ul class="contacts">
      <li class="contacts__item">
        <svg class="contacts__icon" viewBox="0 0 24 24" fill="none" stroke="var(--accent)" stroke-width="1.6">
          <rect x="1" y="1" width="22" height="22" rx="4"/>
          <path d="M8 6.5l2 2.5-1.2 1.4a8 8 0 0 0 4.8 4.8l1.4-1.2 2.5 2-1.4 2c-4.5 0-9.6-5.1-9.6-9.6z" stroke-linejoin="round"/>
        </svg>
        044-987 654 321
      </li>
      <li class="contacts__item">
        <svg class="contacts__icon" viewBox="0 0 24 24" fill="none" stroke="var(--accent)" stroke-width="1.6">
          <rect x="1" y="1" width="22" height="22" rx="4"/>
          <path d="M6 12l12-6-4 13-3-5z" fill="var(--accent)" stroke-linejoin="round"/>
        </svg>
        hello@742build.com
      </li>
      <li class="contacts__item">
        <svg class="contacts__icon" viewBox="0 0 24 24" fill="none" stroke="var(--accent)" stroke-width="1.6">
          <rect x="1" y="1" width="22" height="22" rx="4"/>
          <circle cx="12" cy="12" r="6"/>
          <path d="M6 12h12M12 6c-2.5 3-2.5 9 0 12M12 6c2.5 3 2.5 9 0 12"/>
        </svg>
        www.742build.com
      </li>
    </ul>

    <div class="address">
      <svg class="address__pin" viewBox="0 0 14 19">
        <path d="M7 0a7 7 0 0 0-7 7c0 5 7 12 7 12s7-7 7-12a7 7 0 0 0-7-7z" fill="var(--accent)"/>
        <circle cx="7" cy="7" r="2.6" fill="var(--card)"/>
      </svg>
      4417 Harbor Ridge Blvd, 212-C, FL 32561
    </div>

    <div class="sign-off" role="img" aria-label="Handwritten sign-off: Thank you, have fun"></div>
  </section>
</main>
</body>
</html>
```